Oru Pest Control Booth Backdrop

Looking for a family owned and operated Pest control with safest products for family and pets. Attaching our old design and looking for a new and improved idea. Backdrop is 7.5'x7.5'

```html
<!DOCTYPE html>
<html lang="en">
<head>
<meta charset="utf-8">
<title>Oru Pest Control Booth Backdrop</title>
<link rel="stylesheet" href="https://fonts.googleapis.com/css2?family=Anton&family=Poppins:wght@500;600;700;800&display=swap">
<style>
  :root {
    --stage: #e6e6e6;
    --paper: #ffffff;
    --brand-orange: #e2532a;
    --ink: #141414;
    --peach: #ffe3d2;
    --rule: #dcdcdc;
    --sky: #dbe6ee;
  }
  html, body {
    margin: 0;
    width: 754px;
    height: 1200px;
    overflow: hidden;
    background: var(--stage);
  }
  .backdrop {
    position: absolute;
    left: 27px;
    top: 250px;
    width: 700px;
    height: 700px;
    box-shadow: 0 10px 30px rgba(0,0,0,0.25);
  }
  .backdrop svg { display: block; }
  .brand-name { font-family: "Poppins", sans-serif; font-weight: 800; fill: var(--brand-orange); }
  .headline { font-family: "Anton", sans-serif; fill: var(--paper); }
  .headline-dark { fill: var(--ink); }
  .subline { font-family: "Poppins", sans-serif; font-weight: 800; fill: var(--peach); }
  .badge-top { font-family: "Anton", sans-serif; fill: var(--brand-orange); }
  .badge-bottom { font-family: "Anton", sans-serif; fill: var(--paper); }
  .services-title { font-family: "Poppins", sans-serif; font-weight: 700; fill: var(--ink); }
  .service-label { font-family: "Poppins", sans-serif; font-weight: 600; font-size: 15px; fill: var(--ink); text-anchor: middle; }
  .phone-number { font-family: "Poppins", sans-serif; font-weight: 800; fill: var(--paper); }
  .web-address { font-family: "Poppins", sans-serif; font-weight: 800; fill: var(--paper); }
</style>
</head>
<body>
<div class="backdrop">
  <svg viewBox="0 0 1020 1020" width="700" height="700" xmlns="http://www.w3.org/2000/svg">
    <defs>
      <linearGradient id="photoTones" x1="0" y1="0" x2="0.6" y2="1">
        <stop offset="0" stop-color="#d8e5ee"/>
        <stop offset="0.45" stop-color="#e58a55"/>
        <stop offset="0.8" stop-color="#f2ede8"/>
        <stop offset="1" stop-color="#ffffff"/>
      </linearGradient>
    </defs>

    <rect class="sheet" width="1020" height="1020" fill="var(--paper)"/>

    <!-- hero photo area -->
    <polygon class="hero-photo" role="img" aria-label="Technician in orange hoodie spraying a house wall beside a branded service van"
      points="650,0 1020,0 1020,700 590,700 605,545 478,358" fill="url(#photoTones)"/>
    <polygon class="hero-frame" points="618,0 652,0 478,358 606,545 592,565 444,358" fill="var(--ink)"/>

    <!-- brand -->
    <circle class="brand-dot" cx="58" cy="128" r="18" fill="var(--brand-orange)"/>
    <text class="brand-name" x="88" y="146" font-size="50">Oru Pest Control</text>

    <!-- headline panel -->
    <polygon class="headline-panel" points="0,205 365,205 497,420 365,655 0,655" fill="var(--brand-orange)"/>
    <text class="headline" x="33" y="322" font-size="78">CUTTING</text>
    <text class="headline" x="33" y="395" font-size="78">THE PESTS</text>
    <text class="headline headline-dark" x="35" y="451" font-size="60">OUT OF LIFE</text>
    <line class="headline-rule" x1="40" y1="467" x2="400" y2="467" stroke="var(--peach)" stroke-width="2"/>
    <text class="subline" x="40" y="507" font-size="30">Prevent Future</text>
    <text class="subline" x="40" y="546" font-size="30">Infestations &amp; Get</text>
    <text class="subline" x="40" y="585" font-size="30">Rid of Pests</text>

    <!-- family friendly badge -->
    <g class="badge" transform="translate(445,565)">
      <polygon fill="var(--ink)" stroke="var(--paper)" stroke-width="4"
        points="0,-92 14,-80 31,-86 40,-71 58,-71 62,-54 78,-46 75,-29 89,-17 80,-2 89,14 76,26 79,43 62,51 58,69 40,69 31,84 14,79 0,91 -14,79 -31,84 -40,69 -58,69 -62,51 -79,43 -76,26 -89,14 -80,-2 -89,-17 -75,-29 -78,-46 -62,-54 -58,-71 -40,-71 -31,-86 -14,-80"/>
      <g transform="rotate(-9)">
        <text class="badge-top" x="-2" y="-6" font-size="50" text-anchor="middle">FAMILY</text>
        <text class="badge-bottom" x="4" y="40" font-size="42" text-anchor="middle">FRIENDLY</text>
      </g>
    </g>

    <!-- services -->
    <text class="services-title" x="41" y="698" font-size="31">Our Services Include</text>
    <g class="service-dividers" stroke="var(--rule)" stroke-width="1.5">
      <line x1="160" y1="720" x2="160" y2="825"/>
      <line x1="285" y1="720" x2="285" y2="825"/>
      <line x1="385" y1="720" x2="385" y2="825"/>
      <line x1="505" y1="720" x2="505" y2="825"/>
      <line x1="625" y1="720" x2="625" y2="825"/>
      <line x1="740" y1="720" x2="740" y2="825"/>
      <line x1="855" y1="720" x2="855" y2="825"/>
    </g>
    <g class="service-badges" fill="var(--brand-orange)" stroke="var(--ink)" stroke-width="1.5">
      <polygon transform="translate(104,755)" points="0,-31 27,-15 27,15 0,31 -27,15 -27,-15"/>
      <polygon transform="translate(220,755)" points="0,-31 27,-15 27,15 0,31 -27,15 -27,-15"/>
      <polygon transform="translate(336,755)" points="0,-31 27,-15 27,15 0,31 -27,15 -27,-15"/>
      <polygon transform="translate(451,755)" points="0,-31 27,-15 27,15 0,31 -27,15 -27,-15"/>
      <polygon transform="translate(567,755)" points="0,-31 27,-15 27,15 0,31 -27,15 -27,-15"/>
      <polygon transform="translate(683,755)" points="0,-31 27,-15 27,15 0,31 -27,15 -27,-15"/>
      <polygon transform="translate(799,755)" points="0,-31 27,-15 27,15 0,31 -27,15 -27,-15"/>
      <polygon transform="translate(914,755)" points="0,-31 27,-15 27,15 0,31 -27,15 -27,-15"/>
    </g>
    <g class="service-labels">
      <text class="service-label" x="104" y="809">Ant</text><text class="service-label" x="104" y="827">Control</text>
      <text class="service-label" x="224" y="809">Bee / Wasp</text><text class="service-label" x="224" y="827">Control</text>
      <text class="service-label" x="336" y="809">Bed Bug</text><text class="service-label" x="336" y="827">Control</text>
      <text class="service-label" x="451" y="809">Boxelder</text><text class="service-label" x="451" y="827">&amp; Elm</text><text class="service-label" x="451" y="845">Seed Bugs</text>
      <text class="service-label" x="567" y="809">Cockroach</text><text class="service-label" x="567" y="827">Control</text>
      <text class="service-label" x="683" y="809">Rodent</text><text class="service-label" x="683" y="827">Control</text>
      <text class="service-label" x="799" y="809">Spider</text><text class="service-label" x="799" y="827">Control</text>
      <text class="service-label" x="914" y="809">Commercial</text><text class="service-label" x="914" y="827">Services</text>
    </g>

    <!-- contact bar -->
    <rect class="contact-bar" x="0" y="880" width="1020" height="140" fill="var(--ink)"/>
    <g class="phone-icon" transform="translate(75,940)">
      <circle r="20" fill="var(--brand-orange)" stroke="var(--paper)" stroke-width="2"/>
      <path d="M-8,-9 l5,-2 l4,7 l-3,3 c2,4 4,6 8,8 l3,-3 l7,4 l-2,5 c-12,1 -23,-10 -22,-22 z" fill="var(--paper)"/>
    </g>
    <text class="phone-number" x="103" y="960" font-size="56">208-555-0147</text>
    <path class="web-pill" d="M553,910 H1020 V966 H553 a28,28 0 0 1 0,-56 z" fill="var(--brand-orange)"/>
    <text class="web-address" x="558" y="952" font-size="42">www.orupest.com</text>
  </svg>
</div>
</body>
</html>
```